R.L. Penrose Electric Holiday Party Invitation

We need a cohesive, on-brand holiday party invitation suite for R.L. Penrose Electrical Contractors (slogan Driven by Excellence). Design should include: 1) 5x7" invitation (print + digital), 2) matching RSVP card, and 3) raffle ticket.
Use our brand colors (navy, red, white, light gray) and modern professional style with subtle holiday accents.
Event: Thursday, Dec 18 2025 | 6-10 PM | Ravenna Bellhaven, 318 Quillby Ave, Hammonton NJ 08037.
RSVP by: Dec 1 | Plus one allowed.
Deliver print-ready PDFs + editable source files.

```html
<!DOCTYPE html>
<html lang="en">
<head>
<meta charset="utf-8">
<title>R.L. Penrose Electric – RSVP Card &amp; Raffle Ticket</title>
<link rel="stylesheet" href="https://fonts.googleapis.com/css2?family=Montserrat:wght@400;500;700;800&display=swap">
<style>
  :root {
    --navy: #14264a;
    --red: #dc2232;
    --white: #f6f6f8;
    --card-white: #ffffff;
    --gray: #a9a9ab;
    --branch: #d6d6d6;
    --backdrop: #e6e6e6;
    --shadow: rgba(0, 0, 0, 0.28);
  }
  * { margin: 0; padding: 0; box-sizing: border-box; }
  html, body {
    width: 1200px;
    height: 1200px;
    overflow: hidden;
    background: var(--backdrop);
    font-family: "Montserrat", Arial, sans-serif;
  }
  .canvas { position: relative; width: 1200px; height: 1200px; }

  /* RSVP card */
  .rsvp-card {
    position: absolute;
    left: 304px; top: 256px;
    width: 591px; height: 403px;
    background: var(--navy);
    box-shadow: 6px 6px 6px var(--shadow);
    padding: 12px;
  }
  .rsvp-card__frame {
    width: 100%; height: 100%;
    border: 5px solid var(--red);
    background: var(--white);
    position: relative;
  }
  .brand-dot {
    position: absolute;
    border-radius: 50%;
    background: var(--red);
  }
  .rsvp-card .brand-dot { width: 24px; height: 24px; left: 273px; top: 60px; }
  .brand {
    position: absolute;
    text-align: center;
    line-height: 1;
  }
  .brand__name { color: var(--navy); font-weight: 800; letter-spacing: 0.02em; }
  .brand__trade { color: var(--red); font-weight: 500; letter-spacing: 0.03em; }
  .brand__slogan { color: var(--gray); font-weight: 400; letter-spacing: 0.04em; }

  .rsvp-card .brand { left: 0; width: 100%; top: 110px; }
  .rsvp-card .brand__name { font-size: 41px; }
  .rsvp-card .brand__trade { font-size: 23px; margin-top: 3px; }
  .rsvp-card .brand__slogan { font-size: 19px; margin-top: 1px; }

  .rsvp-card__label {
    position: absolute;
    left: 41px; top: 250px;
    color: var(--red);
    font-weight: 800;
    font-size: 27px;
    letter-spacing: 0.02em;
  }
  .holiday-branches {
    position: absolute;
    background: radial-gradient(ellipse at 50% 100%, var(--branch) 0%, rgba(214,214,214,0.35) 55%, rgba(214,214,214,0) 75%);
  }
  .rsvp-card .holiday-branches { left: 99px; top: 231px; width: 366px; height: 132px; }

  /* Raffle ticket */
  .ticket {
    position: absolute;
    left: 304px; top: 696px;
    width: 596px; height: 252px;
  }
  .ticket__shape {
    position: absolute; inset: 0;
    filter: drop-shadow(5px 5px 4px var(--shadow));
  }
  .ticket .holiday-branches { left: 260px; top: 90px; width: 324px; height: 150px; }
  .ticket .brand-dot { width: 16px; height: 16px; left: 186px; top: 36px; }
  .ticket .brand { left: 56px; width: 276px; top: 88px; }
  .ticket .brand__name { font-size: 24px; }
  .ticket .brand__trade { font-size: 15px; margin-top: 1px; }
  .ticket .brand__slogan { font-size: 13.5px; margin-top: 1px; }
  .ticket__date { color: var(--red); font-weight: 500; font-size: 13.5px; margin-top: 3px; letter-spacing: 0.03em; }
  .ticket__guest { color: var(--navy); font-weight: 500; font-size: 13.5px; margin-top: 2px; letter-spacing: 0.03em; }
  .ticket__name-line {
    position: absolute;
    left: 82px; top: 198px;
    width: 222px; height: 2px;
    background: var(--navy);
  }
  .vertical {
    position: absolute;
    white-space: nowrap;
    transform-origin: center;
  }
  .ticket__rsvp {
    left: 374px; top: 104px;
    width: 100px; height: 30px;
    line-height: 30px; text-align: center;
    transform: rotate(-90deg);
    color: var(--red); font-weight: 800; font-size: 26px;
  }
  .ticket__raffle-pill {
    left: 411px; top: 108px;
    width: 186px; height: 34px;
    transform: rotate(-90deg);
    background: var(--red);
    border-radius: 17px;
    color: var(--card-white);
    font-weight: 500; font-size: 16px; letter-spacing: 0.08em;
    line-height: 34px; text-align: center;
  }
  .ticket__serial {
    left: 500px; top: 98px;
    width: 120px; height: 22px;
    line-height: 22px; text-align: center;
    transform: rotate(-90deg);
    color: var(--navy); font-weight: 500; font-size: 16px; letter-spacing: 0.08em;
  }
</style>
</head>
<body>
<main class="canvas">

  <section class="rsvp-card">
    <div class="rsvp-card__frame">
      <span class="brand-dot"></span>
      <div class="brand">
        <div class="brand__name">R.L. PENROSE</div>
        <div class="brand__trade">Electric Contractors</div>
        <div class="brand__slogan">Driven by Excellence</div>
      </div>
      <div class="rsvp-card__label">RSVP</div>
      <div class="holiday-branches" role="img" aria-label="Faint winter branch illustration"></div>
    </div>
  </section>

  <section class="ticket">
    <svg class="ticket__shape" width="596" height="252" viewBox="0 0 596 252" aria-hidden="true">
      <path d="M12 0 H445 A9 9 0 0 0 463 0 H584 A12 12 0 0 0 596 12 V240 A12 12 0 0 0 584 252 H463 A9 9 0 0 0 445 252 H12 A12 12 0 0 0 0 240 V12 A12 12 0 0 0 12 0 Z" fill="#ffffff"/>
      <rect x="12" y="12" width="572" height="228" fill="#f6f6f8" stroke="#dc2232" stroke-width="2"/>
      <line x1="454" y1="22" x2="454" y2="230" stroke="#dc2232" stroke-width="2" stroke-dasharray="5 4"/>
      <circle cx="454" cy="14" r="6" fill="#f6f6f8" stroke="#dc2232" stroke-width="2"/>
      <circle cx="454" cy="238" r="6" fill="#f6f6f8" stroke="#dc2232" stroke-width="2"/>
    </svg>
    <div class="holiday-branches" role="img" aria-label="Faint winter branch illustration"></div>
    <span class="brand-dot"></span>
    <div class="brand">
      <div class="brand__name">R.L. PENROSE</div>
      <div class="brand__trade">Electric Contractors</div>
      <div class="brand__slogan">Driven by Excellence</div>
      <div class="ticket__date">DEC 1 - 2025</div>
      <div class="ticket__guest">Plus one allowed</div>
    </div>
    <div class="ticket__name-line"></div>
    <div class="vertical ticket__rsvp">RSVP</div>
    <div class="vertical ticket__raffle-pill">RAFFFCIEE</div>
    <div class="vertical ticket__serial">SL:00098</div>
  </section>

</main>
</body>
</html>
```